Brightfold Partners Website

Brightfold Partners (BP) provide Analytics & Enterprise Performance Management (EPM) advisory & consultancy services. We are passionate about data and making a difference for our clients by working in partnership with them, helping them on their journey to becoming an Brightfold Partner. We deliver insights which give our clients a competitive edge and a much deeper understanding of their organisation.

We need a website which shows who we are, what we do and how we do it.

www.brightfold-partners.example is our very basic website at the moment. We want to completely revamp it with a corporate look

```html
<!DOCTYPE html>
<html lang="en">
<head>
<meta charset="utf-8">
<title>Brightfold Partners – Data Analytics & EPM Consulting</title>
<link rel="stylesheet" href="https://fonts.googleapis.com/css2?family=Montserrat:wght@400;500;600;700;800&family=Open+Sans:wght@400;600&display=swap">
<style>
:root{
  --navy:#0e2739;
  --navy-deep:#0a1d2b;
  --panel:#123246;
  --panel-mid:#2b5a73;
  --teal:#3a8db0;
  --teal-light:#6fb6d4;
  --white:#ffffff;
  --muted:#c4d3dd;
  --ghost:rgba(120,160,185,.16);
}
*{margin:0;padding:0;box-sizing:border-box}
html,body{width:1200px;height:2948px;overflow:hidden}
body{background:var(--navy);color:var(--white);font-family:"Open Sans",Arial,sans-serif;position:relative}
.abs{position:absolute}
.brand{display:flex;align-items:center;gap:16px}
.brand-dot{width:60px;height:60px;border-radius:50%;background:var(--white)}
.brand-name{font-family:"Montserrat",Arial,sans-serif;font-weight:700;font-size:26px;line-height:1.05;text-transform:uppercase;letter-spacing:.5px;color:var(--white)}
.nav{display:flex;gap:36px;font-family:"Montserrat",Arial,sans-serif;font-size:15px;font-weight:500;letter-spacing:.5px}
.nav .active{border-left:2px solid var(--white);padding-left:10px}
.btn{display:inline-block;background:var(--white);color:var(--navy);font-family:"Montserrat",Arial,sans-serif;font-weight:600;font-size:13px;border-radius:22px;padding:13px 30px;box-shadow:0 4px 14px rgba(0,0,0,.4)}
.btn-sm{font-size:11px;padding:9px 22px;border-radius:16px}
.ghost{font-family:"Montserrat",Arial,sans-serif;font-weight:800;color:var(--ghost);font-size:92px;letter-spacing:4px}
.h2{font-family:"Montserrat",Arial,sans-serif;font-weight:700;font-size:46px;letter-spacing:1px;text-align:center}
.h2-rule{width:70px;height:3px;background:var(--white);margin:14px auto 0}
.hero-img{right:0;top:0;width:700px;height:560px;background:radial-gradient(ellipse at 70% 45%,#3c7fa3 0%,#1b4a66 35%,#0e2739 72%)}
.hero-title{left:140px;top:210px;font-family:"Montserrat",Arial,sans-serif;font-weight:700;font-size:50px;line-height:1.15}
.hero-sub{left:140px;top:352px;font-family:"Montserrat",Arial,sans-serif;font-weight:600;font-size:19px;line-height:1.45;letter-spacing:1.5px}
.about-photo{left:120px;top:710px;width:270px;height:270px;border-radius:50%;border:8px solid var(--white);background:linear-gradient(135deg,#e9eef2,#9fb6c6 60%,#5e7d92);box-shadow:0 10px 30px rgba(0,0,0,.5)}
.about-text{left:540px;top:810px;width:560px;font-size:14px;line-height:1.6;color:var(--muted)}
.card{top:1362px;width:290px;height:340px;border:3px solid var(--muted);background:var(--panel);text-align:center;padding:26px 22px 0}
.card.mid{background:var(--panel-mid)}
.card h3{font-family:"Montserrat",Arial,sans-serif;font-weight:700;font-size:18px;line-height:1.3;margin:18px 0 20px}
.card p{font-size:12.5px;line-height:1.55;color:var(--muted)}
.card .btn{position:absolute;left:50%;bottom:-20px;transform:translateX(-50%)}
.method{display:flex;gap:26px;width:440px;z-index:2}
.method-icon{flex:none;width:110px;height:110px;border-radius:50%;background:radial-gradient(circle at 40% 35%,#5aa9cb,#2a6d8e 70%);box-shadow:0 0 0 6px rgba(58,141,176,.25);display:flex;align-items:center;justify-content:center}
.method h4{font-family:"Montserrat",Arial,sans-serif;font-weight:600;font-size:15px;line-height:1.35;margin-bottom:10px}
.method p{font-size:12.5px;line-height:1.55;color:var(--muted)}
.method .more{display:block;margin-top:14px;font-family:"Montserrat",Arial,sans-serif;font-size:11px;font-weight:600;color:var(--teal-light)}
.band-img{left:0;top:2250px;width:1200px;height:350px;z-index:0;background:linear-gradient(180deg,rgba(14,39,57,0) 0%,#1f4259 40%,#6f8fa3 70%,#1a3446 100%)}
.footer{left:0;top:2600px;width:1200px;height:348px;background:var(--navy-deep);z-index:3}
.foot-rule{left:140px;width:920px;height:1px;background:rgba(255,255,255,.25)}
.foot-item{display:flex;align-items:center;gap:14px;font-size:14px}
.social{display:flex;gap:12px}
.social span{width:30px;height:30px;border-radius:50%;background:var(--white)}
.legal{font-size:11px;color:var(--muted)}
</style>
</head>
<body>

<header>
  <div class="abs hero-img" role="img" aria-label="Glowing circuit-board technology image"></div>
  <div class="abs brand" style="left:30px;top:22px">
    <span class="brand-dot"></span>
    <span class="brand-name">Brightfold<br>Partners</span>
  </div>
  <nav class="abs nav" style="right:50px;top:52px">
    <span class="active">HOME</span><span>WHO WE ARE</span><span>WHAT WE DO</span><span>HOW WE DO IT</span>
  </nav>
  <h1 class="abs hero-title">BRIGHTFOLD<br>PARTNERS</h1>
  <p class="abs hero-sub">DATA ANALYTICS &amp; EPM<br>CONSULTING SERVICES</p>
  <span class="abs btn" style="left:140px;top:452px">GET STARTED</span>
</header>

<section class="who">
  <div class="abs ghost" style="left:20px;top:600px">ABOUT</div>
  <div class="abs about-photo" role="img" aria-label="Business analytics charts on paper and laptop"></div>
  <h2 class="abs" style="left:640px;top:722px;font-family:Montserrat,Arial,sans-serif;font-weight:700;font-size:46px;letter-spacing:1px">WHO WE ARE</h2>
  <div class="abs" style="left:640px;top:784px;width:70px;height:3px;background:var(--white)"></div>
  <p class="abs about-text">BP are a Data Analytics &amp; EPM company, specialising in the implementation and support of Business Intelligence, EPM and Data Analytics business solutions, both in the Cloud and on-premise. Brightfold Partners is an exciting start up in the Data Analytics and EPM space. Founded in 2015 BP specialise in the implementation and support of BI, EPM and Data Analytics business solutions, both in the Cloud and on-premise. Call us on 01 555 0142 or email hello@brightfold-partners.example for more information.</p>
  <span class="abs btn btn-sm" style="left:540px;top:1028px">READ MORE</span>
</section>

<section class="what">
  <div class="abs ghost" style="left:0;width:1200px;text-align:center;top:1160px">SERVICES</div>
  <div class="abs" style="left:0;width:1200px;top:1218px"><h2 class="h2">WHAT WE DO</h2><div class="h2-rule"></div></div>

  <article class="abs card" style="left:145px">
    <svg width="56" height="56" viewBox="0 0 56 56" fill="none" stroke="#fff" stroke-width="2"><circle cx="28" cy="20" r="9"/><path d="M12 50c2-12 30-12 32 0"/><rect x="36" y="4" width="16" height="11" rx="2"/></svg>
    <h3>ADVISE &amp; ARCHITECT<br>SERVICES</h3>
    <p>Helping our customers understand the art of the possible and safeguarding their investments by partnering implementations.</p>
    <span class="btn btn-sm">READ MORE</span>
  </article>
  <article class="abs card mid" style="left:455px">
    <svg width="56" height="56" viewBox="0 0 56 56" fill="none" stroke="#fff" stroke-width="2"><path d="M28 6l8 22-8 20-8-20z"/><circle cx="28" cy="28" r="3"/><path d="M8 48h40"/></svg>
    <h3>DESIGN<br>&amp; IMPLEMENT</h3>
    <p>Working with the project management team, through each stage of the project, with clearly defined deliverables and well-planned steps to deliver them.</p>
    <span class="btn btn-sm">READ MORE</span>
  </article>
  <article class="abs card" style="left:765px">
    <svg width="56" height="56" viewBox="0 0 56 56" fill="none" stroke="#fff" stroke-width="2"><circle cx="28" cy="28" r="9"/><circle cx="28" cy="28" r="18" stroke-dasharray="6 5"/></svg>
    <h3>OPTIMISE &amp; MANAGE</h3>
    <p>Our Managed Services deliver proactive, on-demand support for EPM and Data Analytics environments, ensuring continuous service improvement through our managed service.</p>
    <span class="btn btn-sm">READ MORE</span>
  </article>
</section>

<div class="abs band-img" role="img" aria-label="Hands using a tablet with data charts"></div>

<section class="how">
  <div class="abs ghost" style="left:0;width:1200px;text-align:center;top:1800px">HOW WE DO IT</div>
  <div class="abs" style="left:0;width:1200px;top:1858px"><h2 class="h2">HOW WE DO IT</h2><div class="h2-rule"></div></div>

  <div class="abs method" style="left:150px;top:1990px">
    <div class="method-icon"><svg width="44" height="44" viewBox="0 0 44 44" fill="none" stroke="#fff" stroke-width="2.5"><circle cx="18" cy="18" r="11"/><path d="M26 26l12 12"/></svg></div>
    <div><h4>ANALYTICS</h4><p>Lorem ipsum dolor sit amet, consectetur adipiscing elit, sed do eiusmod tempor incididunt ut labore et dolore</p><span class="more">READ MORE</span></div>
  </div>
  <div class="abs method" style="left:660px;top:1990px">
    <div class="method-icon"><svg width="44" height="44" viewBox="0 0 44 44" fill="none" stroke="#fff" stroke-width="2.5"><rect x="6" y="24" width="7" height="14"/><rect x="18" y="16" width="7" height="22"/><rect x="30" y="8" width="7" height="30"/></svg></div>
    <div><h4>ENTERPRISE PERFORMANCE<br>MANAGEMENT</h4><p>Lorem ipsum dolor sit amet, consectetur adipiscing elit, sed do eiusmod</p><span class="more">READ MORE</span></div>
  </div>
  <div class="abs method" style="left:150px;top:2170px">
    <div class="method-icon"><svg width="44" height="44" viewBox="0 0 44 44" fill="none" stroke="#fff" stroke-width="2.5"><circle cx="15" cy="14" r="6"/><circle cx="30" cy="14" r="6"/><path d="M4 36c2-10 20-10 22 0M20 36c2-10 18-10 20 0"/></svg></div>
    <div><h4>ADVISORY</h4><p>Lorem ipsum dolor sit amet, consectetur adipiscing elit, sed do eiusmod tempor incididunt ut labore et dolore</p><span class="more">READ MORE</span></div>
  </div>
  <div class="abs method" style="left:660px;top:2170px">
    <div class="method-icon"><svg width="44" height="44" viewBox="0 0 44 44" fill="none" stroke="#fff" stroke-width="2.5"><rect x="6" y="8" width="32" height="22" rx="2"/><path d="M16 38h12M22 30v8"/></svg></div>
    <div><h4>CONSULTANCY SERVICES</h4><p>Lorem ipsum dolor sit amet, consectetur adipiscing elit, sed do eiusmod tempor incididunt ipsum dolor sit amet</p><span class="more">READ MORE</span></div>
  </div>
</section>

<footer class="abs footer">
  <div class="abs brand" style="left:140px;top:40px">
    <span class="brand-dot"></span>
    <span class="brand-name">Brightfold<br>Partners</span>
  </div>
  <nav class="abs nav" style="right:140px;top:64px">
    <span>HOME</span><span>WHO WE ARE</span><span>WHAT WE DO</span><span>HOW WE DO IT</span>
  </nav>
  <div class="abs foot-rule" style="top:150px"></div>
  <div class="abs foot-item" style="left:140px;top:190px">
    <svg width="18" height="24" viewBox="0 0 18 24" fill="#fff"><path d="M9 0a9 9 0 0 0-9 9c0 7 9 15 9 15s9-8 9-15a9 9 0 0 0-9-9zm0 12a3 3 0 1 1 0-6 3 3 0 0 1 0 6z"/></svg>
    <span>12 Harbour Lane, Northgate, Dublin 4, D04 QX21</span>
  </div>
  <div class="abs foot-item" style="right:140px;top:190px">
    <svg width="22" height="16" viewBox="0 0 22 16" fill="none" stroke="#fff" stroke-width="2"><rect x="1" y="1" width="20" height="14"/><path d="M1 1l10 8 10-8"/></svg>
    <span>hello@brightfold-partners.example</span>
  </div>
  <div class="abs foot-rule" style="top:250px"></div>
  <p class="abs legal" style="left:140px;top:292px">© 2022 Brightfold Partners. All rights reserved. Privacy &nbsp;|&nbsp; Terms of Use</p>
  <div class="abs social" style="right:140px;top:284px"><span></span><span></span></div>
</footer>

</body>
</html>
```